HCA Twirl under our moonbeams

My nonprofit social service agency is having a fun gala based on the TV show twirl under moonbeams, and we need the key design for an invitation. The event is a dinner and will have 7 local well-known people dance in a contest-like setting with a nationally known host. This does not need to be the final invitation (RSVP, list of dancers/hosts, etc.). All I need at this point is a great design for the cover to give this event an identity and entice people to attend and/or donate to the cause! Though our logo colors are blue/green/burgandy, this can use black/gold/silver/white as well. Our website is www.hcalorvin.org if that helps explain who we are.

Also, it can be abstract. And it does not have to include ballroom dancers if the word mark or other graphics are eye catching.

Target Market(s)

Donors, upscale, higher income,45-70, men and women (though women will more likely make the decision to attend)

Industry/Entity Type

Tv

Requirements
Must have
• The wording to be incorporated into the invitation cover is:
Harborview Community Aid
Celebrates Stepping Up for Decades with
Twirl Under Moonbeams
hosted by Host Name (will give the final name when confirmed)

Saturday, November 8, 2014
7 pm
Marlowe Cincinnati Crestwood Tower
Nice to have
• I'd like to see something other than ballroom dancers just to give my committee some options. Is it possible to show footprints of dancers (man's shoe with woman's high heels) as the design element? Something that can be used across the invite (rsvp card).
Should not have
• You have free range to create and have fun! If you use our logo colors, either choose one color as the focus, or just be sure to focus on green and burgandy together

```html
<!DOCTYPE html>
<html lang="en">
<head>
<meta charset="utf-8">
<title>Harborview Community Aid – Twirl Under Our Moonbeams</title>
<link rel="stylesheet" href="https://fonts.googleapis.com/css2?family=Great+Vibes&family=Cedarville+Cursive&family=Raleway:wght@400;600;700&family=Pinyon+Script&display=swap">
<style>
  :root {
    --blue-deep: #1f3f8f;
    --blue-mid: #2a63b5;
    --blue-glow: #3a78c8;
    --silver: #c9ccd3;
    --white: #ffffff;
    --shoe-glow: rgba(255, 255, 255, 0.95);
  }
  html, body {
    margin: 0;
    padding: 0;
    width: 927px;
    height: 1200px;
    overflow: hidden;
    background: var(--blue-deep);
  }
  p { margin: 0; }
  .invitation-cover {
    position: relative;
    width: 927px;
    height: 1200px;
    overflow: hidden;
    color: var(--white);
    background: radial-gradient(ellipse 70% 55% at 50% 50%, var(--blue-glow) 0%, var(--blue-mid) 45%, var(--blue-deep) 100%);
    font-family: "Raleway", Arial, sans-serif;
  }
  .frame {
    position: absolute;
    left: 31px;
    top: 31px;
    width: 849px;
    height: 1122px;
    border: 8px solid var(--silver);
  }
  .agency-name {
    position: absolute;
    top: 74px;
    right: 90px;
    display: flex;
    align-items: center;
    gap: 10px;
    font-weight: 600;
    font-size: 22px;
    letter-spacing: -0.2px;
    text-transform: lowercase;
  }
  .agency-mark {
    width: 34px;
    height: 34px;
    border-radius: 50%;
    background: var(--white);
  }
  .celebrates, .stepping-up {
    position: absolute;
    font-family: "Cedarville Cursive", cursive;
    white-space: nowrap;
  }
  .celebrates {
    top: 142px;
    left: 582px;
    font-size: 22px;
  }
  .stepping-up {
    top: 192px;
    left: 398px;
    font-size: 25px;
  }
  .event-title {
    margin: 0;
    font-weight: normal;
  }
  .title-twirl {
    position: absolute;
    top: 222px;
    left: 96px;
    font-family: "Great Vibes", cursive;
    font-size: 182px;
    line-height: 1;
    white-space: nowrap;
    text-shadow: 0 3px 5px rgba(0, 0, 0, 0.35);
  }
  .title-under-our {
    position: absolute;
    top: 312px;
    left: 572px;
    font-weight: 700;
    font-size: 30px;
    letter-spacing: 0.5px;
    text-transform: uppercase;
    white-space: nowrap;
  }
  .title-moonbeams {
    position: absolute;
    top: 392px;
    left: 428px;
    font-family: "Great Vibes", cursive;
    font-size: 104px;
    line-height: 1;
    white-space: nowrap;
    text-shadow: 0 3px 6px rgba(0, 0, 0, 0.45);
  }
  .shoe-illustration {
    position: absolute;
    left: 250px;
    top: 380px;
    width: 450px;
    height: 380px;
    background: radial-gradient(ellipse 48% 40% at 40% 66%, var(--shoe-glow) 0%, rgba(255, 255, 255, 0.7) 45%, rgba(255, 255, 255, 0) 75%);
  }
  .event-details {
    position: absolute;
    left: 31px;
    width: 865px;
    text-align: center;
    text-transform: uppercase;
    font-weight: 400;
    white-space: nowrap;
  }
  .event-date {
    top: 806px;
    font-size: 37px;
    letter-spacing: 0.5px;
  }
  .event-date sup {
    font-size: 18px;
    vertical-align: 16px;
  }
  .event-time {
    top: 862px;
    font-size: 37px;
  }
  .event-time .star {
    font-size: 20px;
    vertical-align: 8px;
    margin: 0 32px;
  }
  .divider {
    position: absolute;
    top: 919px;
    left: 77px;
    width: 773px;
    height: 2px;
    background: var(--white);
  }
  .event-venue {
    top: 938px;
    font-size: 31px;
    letter-spacing: 1px;
  }
  .hosted-by {
    top: 992px;
    font-size: 31px;
    letter-spacing: 1px;
  }
  .host-name {
    position: absolute;
    top: 1048px;
    left: 31px;
    width: 865px;
    text-align: center;
    font-family: "Pinyon Script", cursive;
    font-size: 66px;
    line-height: 1.2;
  }
</style>
</head>
<body>
  <main class="invitation-cover">
    <div class="frame"></div>

    <div class="agency-name">
      <span class="agency-mark"></span>
      <span>harborview community aid...</span>
    </div>

    <p class="celebrates">celebrates</p>
    <p class="stepping-up">Stepping Up for Decades with...</p>

    <div class="shoe-illustration" role="img" aria-label="Glowing white high-heeled dance shoe"></div>

    <h1 class="event-title">
      <span class="title-twirl">Twirl</span>
      <span class="title-under-our">under our</span>
      <span class="title-moonbeams">Moonbeams</span>
    </h1>

    <p class="event-details event-date">November 8<sup>th</sup> 2014</p>
    <p class="event-details event-time"><span class="star">★</span>7:00PM<span class="star">★</span></p>

    <div class="divider"></div>

    <p class="event-details event-venue">Marlowe Cincinnati Crestwood Tower</p>
    <p class="event-details hosted-by">Hosted by:</p>
    <p class="host-name">Name Here</p>
  </main>
</body>
</html>
```